Business Card Design for new consultancy company

Name of Company: Cobalt Wayline
Nature of Business: Digital Business Consultancy
Specialises in Digital Media Strategy, Digital Business Model Transformation, Over-The-Top (OTT) Development, Web Business Development, Digital Marketing, Web and App Product Development, Design and Innovation

Website: http://www.cobalt-wayline.example

Designs can be of any colour or any number of colours, objective is to give the impression we are a digital trend setter, creative and impactful.

Also please suggest a logo to complement the name and business card.

Target Market(s)

Media Companies, Telcos, Enterprises

Industry/Entity Type

Business

Contact Information for Business Card

Standard business card size. OK with to play with small variations like corners for impact/impression.

Font styles to use
Serif
Sans Serif

Requirements
Must have
• Clarity, Impact, Creativity
Nice to have
• Design should encapsulate professionalism, expertise, yet trend-setting and vibrant for digital consultancy
Should not have
• Messy layout, too gaudy colours or design

```html
<!DOCTYPE html>
<html lang="en">
<head>
<meta charset="utf-8">
<title>Cobalt Wayline — Business Card</title>
<link href="https://fonts.googleapis.com/css2?family=Open+Sans:wght@400;600&display=swap" rel="stylesheet">
<style>
  :root {
    --bg: #e6e4e0;
    --card: #fbfbfb;
    --card-edge: #e9e9e9;
    --ink: #1c1c1c;
    --muted: #8b8b8b;
    --rule: #3a3a3a;
    --blue: #2b8fd0;
  }
  * { box-sizing: border-box; margin: 0; padding: 0; }
  html, body { width: 1200px; height: 885px; overflow: hidden; }
  body {
    background: var(--bg);
    font-family: "Open Sans", Arial, sans-serif;
    color: var(--ink);
    display: flex;
    align-items: center;
    justify-content: center;
    gap: 50px;
  }
  .card {
    width: 540px;
    height: 315px;
    border-radius: 18px;
    background: linear-gradient(160deg, #ffffff 0%, var(--card) 55%, var(--card-edge) 100%);
    box-shadow: 0 10px 28px rgba(0,0,0,.18);
    position: relative;
  }

  /* brand block */
  .brand { display: flex; flex-direction: column; gap: 6px; }
  .brand__mark { display: flex; align-items: center; gap: 10px; }
  .brand__dot { width: 14px; height: 14px; border-radius: 50%; background: var(--blue); flex: none; }
  .brand__name { font-size: 26px; font-weight: 400; line-height: 1.1; color: var(--ink); }
  .brand__tagline { font-size: 12px; color: var(--muted); padding-left: 24px; }

  /* front */
  .card--front .brand { position: absolute; left: 34px; top: 58px; }
  .person { position: absolute; right: 34px; top: 58px; text-align: right; }
  .person__name { font-size: 17px; letter-spacing: 1px; font-weight: 400; }
  .person__role { font-size: 11px; color: var(--muted); letter-spacing: .4px; margin-top: 2px; }
  .divider {
    position: absolute; left: 170px; right: 34px; top: 148px;
    height: 1px; background: var(--rule);
  }
  .contacts { position: absolute; left: 34px; bottom: 40px; list-style: none; }
  .contacts li { display: flex; align-items: center; gap: 9px; font-size: 12.5px; color: var(--muted); margin-top: 6px; }
  .icon { width: 16px; height: 16px; flex: none; }
  .address { position: absolute; right: 34px; bottom: 44px; text-align: right; font-size: 12px; color: var(--muted); line-height: 1.55; }

  /* back */
  .card--back { display: flex; flex-direction: column; align-items: center; justify-content: center; gap: 26px; }
  .card--back .brand { align-items: center; }
  .card--back .brand__tagline { padding-left: 0; }
  .services {
    width: 430px;
    text-align: center;
    font-size: 12.5px;
    line-height: 1.6;
    color: var(--muted);
  }
</style>
</head>
<body>
  <section class="card card--front" aria-label="Card front">
    <div class="brand">
      <div class="brand__mark">
        <span class="brand__dot"></span>
        <span class="brand__name">Cobalt Wayline</span>
      </div>
      <div class="brand__tagline">Digital business consultancy</div>
    </div>
    <div class="person">
      <div class="person__name">MARCUS ELLERY</div>
      <div class="person__role">Managing Director</div>
    </div>
    <div class="divider"></div>
    <ul class="contacts">
      <li>
        <svg class="icon" viewBox="0 0 16 16"><rect width="16" height="16" rx="3" fill="var(--blue)"/><path d="M5 4h2l1 2.5-1.2 1a6 6 0 0 0 1.7 1.7l1-1.2L12 9v2a1 1 0 0 1-1 1A7 7 0 0 1 4 5a1 1 0 0 1 1-1z" fill="#fff"/></svg>
        0098 7654 321
      </li>
      <li>
        <svg class="icon" viewBox="0 0 16 16"><rect width="16" height="16" rx="3" fill="var(--blue)"/><rect x="3.5" y="5" width="9" height="6.5" fill="none" stroke="#fff" stroke-width="1.2"/><path d="M3.5 5 8 8.6 12.5 5" fill="none" stroke="#fff" stroke-width="1.2"/></svg>
        hello@cobalt-wayline.example
      </li>
      <li>
        <svg class="icon" viewBox="0 0 16 16"><rect width="16" height="16" rx="3" fill="var(--blue)"/><circle cx="8" cy="8" r="4.6" fill="none" stroke="#fff" stroke-width="1.1"/><ellipse cx="8" cy="8" rx="2" ry="4.6" fill="none" stroke="#fff" stroke-width="1"/><path d="M3.4 8h9.2" stroke="#fff" stroke-width="1"/></svg>
        www.cobalt-wayline.example
      </li>
    </ul>
    <div class="address">48 Harbour Lane<br>NSW, 2222, Australia</div>
  </section>

  <section class="card card--back" aria-label="Card back">
    <div class="brand">
      <div class="brand__mark">
        <span class="brand__dot"></span>
        <span class="brand__name">Cobalt Wayline</span>
      </div>
      <div class="brand__tagline">Digital business consultancy</div>
    </div>
    <p class="services">Specialises in Digital Media Strategy, Digital Business Model Transformation, Over-The-Top (OTT) Development, Web Business Development, Digital Marketing, Web and App Product Development, Design and Innovation</p>
  </section>
</body>
</html>
```